Innovative Event Ticketing Start Up. Needs a Web Design

We need a web design for a new company based in London called 'Bandwick'. We are a platform which facilitates the building of groups of customers for events. As more people commit to an event, the price incrementally decreases. We would like there to be an emphasis on the sharing element and the decreasing price with higher participation.

Any quieres please email me at rlvo57@mailtrove.net

Target Market(s)

18-30 year olds who are active and savvy across social media sites

Industry/Entity Type

Events

Number of Pages Required

3 page

Font styles to use
Other font styles liked:
• Phi Roman

Requirements
Must have
• Each event offering runs for a limited time so a countdown timer is also to be included as well as a counter of number of participants (please find example attached).
• The interface needs to have the options for 'Live 'Music', 'Nightlife', 'Festivals', 'Comedy' and 'Everything Else'. Also
• A 'featured' section, for our promoted events
• Social sharing icons for Chatterbarn, Quillow, PingMesh, SMS and Email
• Room the inclusion of a video
• Pages for clients to sign up - registering details ect.
• Content is still being completed, so room available to add when ready
Nice to have
• An interface design we like as a guiding templates on is https://kumvoxapp.com/
• Zamo wordpress theme is also of interest.
• Scroll over clicking for main interface and also for the event once clicked upon.
• Event pages similar desgin to kumvox with same features such as Trelvo Charts but also participant counter and affiliate marketing options.
Should not have
• CMS no longer necessary

```html
<!DOCTYPE html>
<html lang="en">
<head>
<meta charset="utf-8">
<title>Bandwick — Events</title>
<link rel="stylesheet" href="https://fonts.googleapis.com/css2?family=Questrial&family=Open+Sans:wght@400;600;700&display=swap">
<style>
:root{
  --orange:#e9552f;
  --orange-soft:#f3a58e;
  --ink:#3b3b3b;
  --muted:#8a8a8a;
  --line:#e3e3e3;
  --dark:#404047;
  --dark-card:#4d4d55;
  --footer:#2f2f33;
  --white:#ffffff;
  --field:#f4f4f4;
}
*{box-sizing:border-box;margin:0;padding:0}
html,body{width:1200px;height:2720px;overflow:hidden}
body{font-family:"Open Sans",Arial,sans-serif;color:var(--ink);background:var(--white)}
h1,h2,h3,.nav,.btn,.ring-num{font-family:"Questrial","Helvetica Neue",sans-serif}

/* header */
.site-header{height:72px;display:flex;align-items:center;padding:0 88px;background:var(--white);position:relative;z-index:2}
.brand{display:flex;align-items:center;gap:10px;font-family:"Questrial",sans-serif;font-size:24px;color:var(--orange);letter-spacing:1px}
.brand-mark{width:30px;height:30px;background:var(--orange)}
.nav{margin-left:auto;display:flex;align-items:center;gap:30px;font-size:13px;letter-spacing:1px;color:var(--ink)}
.nav .current{color:var(--orange)}
.nav .sign-in{background:#6d6d72;color:var(--white);padding:10px 18px}

/* hero */
.hero{height:508px;position:relative;background:linear-gradient(180deg,#c9d9e4 0%,#d9c3b4 45%,#8d6a5c 100%);text-align:center;padding-top:78px}
.hero-photo{position:absolute;inset:0;background:radial-gradient(circle at 8% 30%,rgba(240,170,120,.55),transparent 30%),radial-gradient(circle at 90% 40%,rgba(235,130,110,.45),transparent 30%),linear-gradient(180deg,rgba(220,230,240,.2),rgba(90,60,50,.35))}
.hero-copy{position:relative}
.hero h1{font-size:44px;font-weight:400;letter-spacing:2px;color:#2d2d2d}
.hero p{width:560px;margin:14px auto 0;font-size:14px;line-height:22px;color:#3e3e3e}
.btn{display:inline-block;font-size:14px;letter-spacing:1px;padding:12px 30px}
.btn-outline{border:2px solid var(--orange);color:var(--orange);background:rgba(255,255,255,.75);margin-top:26px}

/* section headings */
.section-title{font-size:26px;font-weight:400;letter-spacing:2px;text-align:center}
.rule{width:60px;height:2px;background:var(--orange);margin:14px auto 18px}
.lead{width:720px;margin:0 auto;text-align:center;font-size:13px;line-height:21px;color:var(--muted)}

/* welcome */
.welcome{height:480px;padding-top:26px;text-align:center}
.welcome-mark{width:30px;height:30px;background:var(--orange);margin:0 auto 20px}
.categories{display:flex;justify-content:center;gap:100px;margin-top:34px}
.category{width:100px;text-align:center}
.category-icon{width:64px;height:64px;border-radius:50%;background:#f6f1ec;margin:0 auto 10px;display:flex;align-items:center;justify-content:center}
.category-label{font-family:"Questrial",sans-serif;font-size:17px;color:var(--orange);letter-spacing:1px}
.more-link{display:block;margin-top:34px;font-size:12px;font-weight:700;color:var(--ink);letter-spacing:1px;text-decoration:underline}
.more-note{margin-top:10px;font-size:12px;color:var(--muted)}

/* featured */
.featured{height:580px;background:var(--dark);padding-top:50px;color:var(--white)}
.featured .section-title{color:var(--white)}
.featured .lead{color:#b5b5bb}
.event-cards{display:flex;gap:22px;justify-content:center;margin-top:40px}
.event-card{width:236px;background:var(--dark-card)}
.event-photo{height:120px;background:linear-gradient(135deg,#7a4a3c,#c98a60 55%,#3b3550)}
.event-photo.alt{background:linear-gradient(135deg,#2f4f6b,#8fa7b8 55%,#c9b69c)}
.event-body{padding:12px 14px 14px;font-size:12px;line-height:22px}
.event-title{font-weight:600;font-size:13px;margin-bottom:4px}
.event-row{display:flex;align-items:center;gap:8px;color:#d6d6da}
.event-row svg{flex:none}
.event-foot{display:flex;justify-content:space-between;margin-top:6px;padding-top:6px;border-top:1px solid #5e5e66;color:#d6d6da}
.dots{display:flex;justify-content:center;gap:8px;margin-top:26px}
.dots span{width:6px;height:6px;border-radius:50%;background:#77777f}
.dots .on{background:var(--orange)}

/* countdown */
.countdown{height:380px;padding-top:38px}
.rings{display:flex;justify-content:center;gap:100px;margin-top:30px}
.ring{width:124px;height:124px;position:relative}
.ring svg{position:absolute;inset:0}
.ring-text{position:absolute;inset:0;display:flex;flex-direction:column;align-items:center;justify-content:center}
.ring-num{font-size:32px;color:var(--ink)}
.ring-label{font-size:11px;letter-spacing:1px;color:var(--muted)}

/* band */
.promo-band{height:140px;position:relative;background:linear-gradient(90deg,#e8d5cd 0%,#f4e6df 50%,#e7c8bd 100%);text-align:center;padding-top:38px}
.promo-band h3{font-size:22px;font-weight:400;letter-spacing:2px}
.promo-band p{font-size:12px;color:var(--muted);margin-top:8px}
.promo-band a{display:block;font-size:12px;color:var(--orange);margin-top:6px}
.promo-photo{position:absolute;right:0;top:0;width:280px;height:140px;background:radial-gradient(circle at 70% 90%,#c0392b 0,#c0392b 22%,rgba(192,57,43,0) 23%),linear-gradient(90deg,rgba(231,200,189,0),#d9b0a4)}

/* video + register */
.media-register{height:400px;display:flex;gap:80px;padding:40px 88px 0}
.video-block,.register-block{flex:1}
.block-title{font-family:"Questrial",sans-serif;font-size:24px;letter-spacing:1px;margin-bottom:16px}
.video-frame{height:220px;position:relative;background:linear-gradient(180deg,#3a2b2a,#8a5b3f 55%,#d9a56a)}
.video-bar{position:absolute;left:0;right:0;top:0;height:26px;background:rgba(0,0,0,.45)}
.play{position:absolute;left:50%;top:50%;width:56px;height:40px;margin:-20px 0 0 -28px;background:rgba(0,0,0,.7);border-radius:8px;display:flex;align-items:center;justify-content:center}
.video-caption{font-size:12px;color:var(--muted);margin-top:12px}
.video-caption span{color:var(--orange);text-decoration:underline}
.form-grid{display:grid;grid-template-columns:1fr 1fr;gap:12px}
.field{height:40px;background:var(--field);border:1px solid var(--line);font-size:12px;color:#a3a3a3;padding:12px}
.field.wide{grid-column:1/3;height:96px}
.btn-solid{background:var(--orange);color:var(--white);font-size:13px;padding:10px 22px;float:right;margin-top:12px}

/* footer */
.site-footer{height:180px;background:var(--footer);text-align:center;padding-top:40px;margin-top:20px}
.share{display:flex;justify-content:center;gap:10px}
.share-item{width:52px;height:52px;display:flex;align-items:center;justify-content:center;font-size:8px;color:var(--white);font-weight:600}
.share-item.c1{background:#3b5a9a}
.share-item.c2{background:#2aa9e0}
.share-item.c3{background:#3fbf4a}
.share-item.c4{background:#e9552f}
.share-item.c5{background:#8a8a90}
.copyright{font-size:12px;color:#9c9ca2;margin-top:26px}
</style>
</head>
<body>

<header class="site-header">
  <div class="brand"><span class="brand-mark"></span>BANDWICK</div>
  <nav class="nav">
    <span class="current">HOME</span><span>ABOUT</span><span>MUSIC</span><span>LIFE</span><span>FESTIVALS</span><span>COMEDY</span><span>JOIN US</span><span class="sign-in">SIGN IN</span>
  </nav>
</header>

<section class="hero">
  <div class="hero-photo" role="img" aria-label="Festival crowd with raised hands and colourful balloons"></div>
  <div class="hero-copy">
    <h1>ACCUSANTIUM DOLOREMQUE</h1>
    <p>Quis autem vel eum iure reprehenderit qui in ea voluptate velit esse quam nihil molestiae consequatur, vel illum qui dolorem.</p>
    <span class="btn btn-outline">JOIN WITH US</span>
  </div>
</section>

<section class="welcome">
  <div class="welcome-mark"></div>
  <h2 class="section-title">WELCOME TO BANDWICK</h2>
  <div class="rule"></div>
  <p class="lead">Sed ut perspiciatis unde omnis iste natus error sit voluptatem accusantium doloremque laudantium, totam rem aperiam, eaque ipsa quae ab illo inventore veritatis et quasi architecto beatae vitae dicta sunt explicabo nemo enim ipsam voluptatem quia voluptas sit aspernatur aut odit.</p>
  <div class="categories">
    <div class="category">
      <div class="category-icon"><svg width="30" height="30" viewBox="0 0 30 30" fill="none" stroke="#6b6b6b" stroke-width="2"><path d="M5 18a10 10 0 0 1 20 0"/><rect x="3" y="17" width="5" height="8" rx="1"/><rect x="22" y="17" width="5" height="8" rx="1"/></svg></div>
      <div class="category-label">LIVE MUSIC</div>
    </div>
    <div class="category">
      <div class="category-icon"><svg width="30" height="30" viewBox="0 0 30 30" fill="none" stroke="#c9912e" stroke-width="2"><rect x="7" y="8" width="13" height="17" rx="1"/><path d="M20 12h3v8h-3"/></svg></div>
      <div class="category-label">NIGHT LIFE</div>
    </div>
    <div class="category">
      <div class="category-icon"><svg width="30" height="30" viewBox="0 0 30 30" fill="none" stroke="#c9912e" stroke-width="2"><path d="M15 4l10 18H5z"/><path d="M15 4v22"/></svg></div>
      <div class="category-label">FESTIVALS</div>
    </div>
    <div class="category">
      <div class="category-icon"><svg width="30" height="30" viewBox="0 0 30 30" fill="none" stroke="#c9912e" stroke-width="2"><circle cx="15" cy="15" r="10"/><path d="M10 17q5 5 10 0"/></svg></div>
      <div class="category-label">COMEDY</div>
    </div>
  </div>
  <span class="more-link">SHOW OTHER OPTIONS</span>
  <p class="more-note">Excepteur sint occaecat cupidatat non proident, sunt in culpa qui officia deserunt.</p>
</section>

<section class="featured">
  <h2 class="section-title">FEATURED EVENTS</h2>
  <div class="rule"></div>
  <p class="lead">Sed ut perspiciatis unde omnis iste natus error sit voluptatem accusantium doloremque laudantium, totam rem aperiam eaque ipsa quae ab illo inventore.</p>
  <div class="event-cards">
    <article class="event-card">
      <div class="event-photo" role="img" aria-label="Concert stage with crowd"></div>
      <div class="event-body">
        <div class="event-title">At vero eos et accusamus et iusto</div>
        <div class="event-row"><svg width="12" height="12" viewBox="0 0 12 12" fill="none" stroke="#e9552f"><rect x="1" y="2" width="10" height="9"/><path d="M1 5h10"/></svg>Saturday 26 September, 2020</div>
        <div class="event-row"><svg width="12" height="12" viewBox="0 0 12 12" fill="none" stroke="#e9552f"><circle cx="6" cy="6" r="5"/><path d="M6 3v3l2 1"/></svg>7:00 pm onwards</div>
        <div class="event-row">1200 People Participating</div>
        <div class="event-foot"><span>Affiliate marketing</span><span>Lorem Ipsum</span></div>
      </div>
    </article>
    <article class="event-card">
      <div class="event-photo alt" role="img" aria-label="Outdoor festival tents"></div>
      <div class="event-body">
        <div class="event-title">At vero eos et accusamus et iusto</div>
        <div class="event-row"><svg width="12" height="12" viewBox="0 0 12 12" fill="none" stroke="#e9552f"><rect x="1" y="2" width="10" height="9"/><path d="M1 5h10"/></svg>Saturday 26 September, 2020</div>
        <div class="event-row"><svg width="12" height="12" viewBox="0 0 12 12" fill="none" stroke="#e9552f"><circle cx="6" cy="6" r="5"/><path d="M6 3v3l2 1"/></svg>7:00 pm onwards</div>
        <div class="event-row">1200 People Participating</div>
        <div class="event-foot"><span>Affiliate marketing</span><span>Lorem Ipsum</span></div>
      </div>
    </article>
    <article class="event-card">
      <div class="event-photo" role="img" aria-label="Dinner party hall with lights"></div>
      <div class="event-body">
        <div class="event-title">At vero eos et accusamus et iusto</div>
        <div class="event-row"><svg width="12" height="12" viewBox="0 0 12 12" fill="none" stroke="#e9552f"><rect x="1" y="2" width="10" height="9"/><path d="M1 5h10"/></svg>Saturday 26 September, 2020</div>
        <div class="event-row"><svg width="12" height="12" viewBox="0 0 12 12" fill="none" stroke="#e9552f"><circle cx="6" cy="6" r="5"/><path d="M6 3v3l2 1"/></svg>7:00 pm onwards</div>
        <div class="event-row">1200 People Participating</div>
        <div class="event-foot"><span>Affiliate marketing</span><span>Lorem Ipsum</span></div>
      </div>
    </article>
    <article class="event-card">
      <div class="event-photo alt" role="img" aria-label="Comedy club audience"></div>
      <div class="event-body">
        <div class="event-title">At vero eos et accusamus et iusto</div>
        <div class="event-row"><svg width="12" height="12" viewBox="0 0 12 12" fill="none" stroke="#e9552f"><rect x="1" y="2" width="10" height="9"/><path d="M1 5h10"/></svg>Saturday 26 September, 2020</div>
        <div class="event-row"><svg width="12" height="12" viewBox="0 0 12 12" fill="none" stroke="#e9552f"><circle cx="6" cy="6" r="5"/><path d="M6 3v3l2 1"/></svg>7:00 pm onwards</div>
        <div class="event-row">1200 People Participating</div>
        <div class="event-foot"><span>Affiliate marketing</span><span>Lorem Ipsum</span></div>
      </div>
    </article>
  </div>
  <div class="dots"><span></span><span class="on"></span><span></span></div>
</section>

<section class="countdown">
  <h2 class="section-title">COUNTDOWN OF OUR EVENTS</h2>
  <div class="rule"></div>
  <p class="lead">Sed ut perspiciatis unde omnis iste natus error sit voluptatem accusantium doloremque laudantium, totam rem aperiam eaque ipsa quae ab illo inventore.</p>
  <div class="rings">
    <div class="ring">
      <svg viewBox="0 0 124 124"><circle cx="62" cy="62" r="54" fill="none" stroke="#eeeeee" stroke-width="10"/><circle cx="62" cy="62" r="54" fill="none" stroke="#e9552f" stroke-width="10" stroke-dasharray="250 340" transform="rotate(-90 62 62)"/></svg>
      <div class="ring-text"><span class="ring-num">38</span><span class="ring-label">DAYS LEFT</span></div>
    </div>
    <div class="ring">
      <svg viewBox="0 0 124 124"><circle cx="62" cy="62" r="54" fill="none" stroke="#eeeeee" stroke-width="10"/><circle cx="62" cy="62" r="54" fill="none" stroke="#e9552f" stroke-width="10" stroke-dasharray="290 340" transform="rotate(-90 62 62)"/></svg>
      <div class="ring-text"><span class="ring-num">4</span><span class="ring-label">DAYS EVENT</span></div>
    </div>
    <div class="ring">
      <svg viewBox="0 0 124 124"><circle cx="62" cy="62" r="54" fill="none" stroke="#eeeeee" stroke-width="10"/><circle cx="62" cy="62" r="54" fill="none" stroke="#e9552f" stroke-width="10" stroke-dasharray="220 340" transform="rotate(-90 62 62)"/></svg>
      <div class="ring-text"><span class="ring-num">680</span><span class="ring-label">PEOPLE JOIN</span></div>
    </div>
    <div class="ring">
      <svg viewBox="0 0 124 124"><circle cx="62" cy="62" r="54" fill="none" stroke="#eeeeee" stroke-width="10"/><circle cx="62" cy="62" r="54" fill="none" stroke="#e9552f" stroke-width="10" stroke-dasharray="270 340" transform="rotate(-90 62 62)"/></svg>
      <div class="ring-text"><span class="ring-num">60</span><span class="ring-label">SEATS LEFT</span></div>
    </div>
  </div>
</section>

<section class="promo-band">
  <div class="promo-photo" role="img" aria-label="Red inflatable ring in a soft pink backdrop"></div>
  <h3>NEMO ENIM IPSAM VOLUPTATEM VOLUPTAS</h3>
  <p>At vero eos et accusamus et iusto</p>
  <a>Click here to join</a>
</section>

<section class="media-register">
  <div class="video-block">
    <div class="block-title">WATCH OUR VIDEO</div>
    <div class="video-frame" role="img" aria-label="Video still of a banquet hall event">
      <div class="video-bar"></div>
      <div class="play"><svg width="18" height="18" viewBox="0 0 18 18"><path d="M4 2l12 7-12 7z" fill="#fff"/></svg></div>
    </div>
    <p class="video-caption">Sed ut perspiciatis unde omnis iste natus <span>error sit</span> voluptatem.</p>
  </div>
  <div class="register-block">
    <div class="block-title">REGISTER NOW!</div>
    <div class="form-grid">
      <div class="field">Enter First Name</div>
      <div class="field">Enter Last Name</div>
      <div class="field">Email</div>
      <div class="field">Phone</div>
      <div class="field wide">Message</div>
    </div>
    <span class="btn btn-solid">Register</span>
  </div>
</section>

<footer class="site-footer">
  <div class="share">
    <span class="share-item c1">Chatterbarn</span>
    <span class="share-item c2">Quillow</span>
    <span class="share-item c3">PingMesh</span>
    <span class="share-item c4">SMS</span>
    <span class="share-item c5">Email</span>
  </div>
  <p class="copyright">Copyright © 2015 Bandwick . All Rights Reserved Privacy Policy</p>
</footer>

</body>
</html>
```